business card

Business card for new business.
Red and black corporate colors.
Card can have an Indsutrial feel to it. Feel free to add Rust, Bolted steel, or graphics as you see fit. We provide highly specialized services to the below mentioned industries.
Keep information out of corners so that if I want I can choose rounded corners.
Information
- front. name - title - phone - email
- Rear
Refining - Rail - Infrastructure - Mining - Energy
Calgary - Edmonton - Fort McMurray - Revelstoke - Vancouver

```html
<!DOCTYPE html>
<html lang="en">
<head>
<meta charset="utf-8">
<title>Girderline business card</title>
<link href="https://fonts.googleapis.com/css2?family=Lato:wght@400;700;900&display=swap" rel="stylesheet">
<style>
  :root {
    --stage: #5a5a5a;
    --card-black: #050505;
    --card-white: #ffffff;
    --brand-red: #e3202a;
    --brand-grey: #8a8a8a;
    --ink: #1c1c1c;
    --light-text: #f2f2f2;
  }
  * { box-sizing: border-box; margin: 0; padding: 0; }
  html, body { width: 1200px; height: 1059px; overflow: hidden; }
  body {
    background: var(--stage);
    font-family: "Lato", sans-serif;
    position: relative;
  }
  .card {
    position: absolute;
    width: 720px;
    height: 410px;
    box-shadow: 0 10px 30px rgba(0,0,0,0.45);
    overflow: hidden;
  }
  .wordmark {
    display: flex;
    align-items: center;
    gap: 14px;
    font-weight: 900;
    color: var(--brand-grey);
    letter-spacing: 1px;
    white-space: nowrap;
  }
  .wordmark-square {
    width: 22px; height: 22px;
    background: var(--brand-red);
    flex: none;
  }

  /* Rear side */
  .card-rear { left: 120px; top: 80px; background: var(--card-black); }
  .card-rear .wordmark {
    position: absolute; left: 0; right: 0; top: 120px;
    justify-content: center; font-size: 64px;
  }
  .service-lines {
    position: absolute; left: 0; right: 0; top: 255px;
    text-align: center; color: var(--light-text);
    font-size: 19px; line-height: 1.55; white-space: nowrap;
  }
  .dot {
    display: inline-block; width: 6px; height: 6px; border-radius: 50%;
    background: var(--brand-red); vertical-align: middle; margin: 0 7px;
  }

  /* Front side */
  .card-front { left: 360px; top: 560px; background: var(--card-white); }
  .contact-panel { position: absolute; left: 0; top: 0; width: 440px; height: 100%; }
  .card-front .wordmark {
    position: absolute; left: 48px; top: 48px; font-size: 40px;
  }
  .address {
    position: absolute; left: 48px; top: 200px;
    font-size: 20px; line-height: 1.3; color: var(--ink);
  }
  .contact-list {
    position: absolute; left: 48px; top: 272px; list-style: none;
    font-size: 20px; line-height: 1.35; color: var(--ink);
  }
  .contact-list li { display: flex; align-items: center; gap: 12px; }
  .contact-list svg { width: 16px; height: 16px; flex: none; }
  .name-panel {
    position: absolute; left: 440px; top: 0; width: 250px; height: 100%;
    background: var(--card-black);
  }
  .person-name {
    position: absolute; left: 26px; top: 42px;
    color: var(--brand-red); font-size: 26px; font-weight: 400; white-space: nowrap;
  }
  .person-title {
    position: absolute; left: 26px; top: 78px;
    color: var(--light-text); font-size: 16px;
  }
  .edge-rule {
    position: absolute; left: 704px; top: 0; width: 2px; height: 100%;
    background: var(--brand-red);
  }
</style>
</head>
<body>
  <section class="card card-rear" aria-label="Card rear">
    <div class="wordmark"><span class="wordmark-square"></span>GIRDERLINE</div>
    <p class="service-lines">
      Fabrication<span class="dot"></span>Pipeline<span class="dot"></span>Utilities<span class="dot"></span>Marine<span class="dot"></span>Power<br>
      Northgate<span class="dot"></span>Ridgeford<span class="dot"></span>Port Alder<span class="dot"></span>Kestrel Falls<span class="dot"></span>Brightwater
    </p>
  </section>

  <section class="card card-front" aria-label="Card front">
    <div class="contact-panel">
      <div class="wordmark"><span class="wordmark-square"></span>GIRDERLINE</div>
      <p class="address">418 Millrace Road<br>Denver, CO 80204</p>
      <ul class="contact-list">
        <li>
          <svg viewBox="0 0 16 16" aria-hidden="true"><path d="M3 1.5l3 3-1.6 1.8a9 9 0 0 0 5.3 5.3L11.5 10l3 3-1.8 1.8C7 15 1 9 1.2 3.3z" fill="#e3202a"/></svg>
          555 014 2290
        </li>
        <li>
          <svg viewBox="0 0 16 16" aria-hidden="true"><rect x="1" y="3" width="14" height="10" fill="#e3202a"/><path d="M1 3l7 6 7-6" stroke="#fff" stroke-width="1.3" fill="none"/></svg>
          info@girderline.com
        </li>
        <li>
          <svg viewBox="0 0 16 16" aria-hidden="true"><circle cx="8" cy="8" r="7" fill="#e3202a"/><path d="M1 8h14M8 1v14M3 4h10M3 12h10" stroke="#fff" stroke-width="1"/></svg>
          www.girderline.com
        </li>
      </ul>
    </div>
    <div class="name-panel">
      <h1 class="person-name">Dana Whitlow</h1>
      <p class="person-title">Manager</p>
    </div>
    <div class="edge-rule"></div>
  </section>
</body>
</html>
```